New Webpage for High Class Expert Witness Services Company

We are looking for a minimalist design for a webpage that just has our logo and an entry form offer to connect with one of our Liaisons.
The entry form should just ask for Name, Email, Contact Info and Description of Project.

Company Name is: The Marlow Crest Advisory Services

Number of Pages Required

1 page

```html
<!DOCTYPE html>
<html lang="en">
<head>
<meta charset="UTF-8">
<title>The Marlow Crest Advisory Services – Connect With Us</title>
<link rel="stylesheet" href="https://fonts.googleapis.com/css2?family=Cinzel:wght@400;500&family=Inter:wght@400&family=Montserrat:wght@500&display=swap">
<style>
  :root {
    --page-bg: #151515;
    --ink-light: #e9e9ea;
    --ink-muted: #d8d8d8;
    --gold: #d4b676;
    --gold-text: #e2c27a;
    --field-bg: #ffffff;
    --field-placeholder: #6b6b6b;
    --divider: #8a8a8a;
  }
  * { box-sizing: border-box; margin: 0; padding: 0; }
  html, body {
    width: 1200px;
    height: 1200px;
    overflow: hidden;
    background: var(--page-bg);
  }
  .page {
    width: 1200px;
    height: 1200px;
    background: var(--page-bg);
    display: flex;
    flex-direction: column;
    align-items: center;
    padding-top: 300px;
  }
  .brand {
    display: flex;
    align-items: center;
    gap: 16px;
  }
  .brand-mark {
    width: 22px;
    height: 22px;
    background: var(--ink-light);
  }
  .brand-name {
    font-family: "Cinzel", serif;
    font-weight: 400;
    font-size: 30px;
    letter-spacing: 1px;
    color: var(--ink-light);
  }
  .brand-divider {
    width: 360px;
    height: 1px;
    background: var(--divider);
    margin-top: 34px;
  }
  .connect-title {
    font-family: "Cinzel", serif;
    font-weight: 400;
    font-size: 30px;
    letter-spacing: 1.5px;
    color: var(--gold-text);
    margin-top: 44px;
  }
  .connect-intro {
    font-family: "Inter", sans-serif;
    font-size: 17px;
    line-height: 30px;
    color: var(--ink-muted);
    text-align: center;
    margin-top: 22px;
  }
  .connect-form {
    width: 960px;
    margin-top: 32px;
    display: grid;
    grid-template-columns: 1fr 1fr;
    gap: 12px;
  }
  .field {
    height: 46px;
    border: none;
    border-radius: 6px;
    background: var(--field-bg);
    font-family: "Inter", sans-serif;
    font-size: 13px;
    color: var(--field-placeholder);
    padding: 0 16px;
  }
  .field::placeholder { color: var(--field-placeholder); }
  .field-details {
    grid-column: 1 / -1;
    height: 86px;
    padding: 12px 16px;
    resize: none;
  }
  .submit-button {
    grid-column: 1 / -1;
    height: 64px;
    border: none;
    background: var(--gold);
    color: #ffffff;
    font-family: "Montserrat", sans-serif;
    font-weight: 500;
    font-size: 16px;
    letter-spacing: 1px;
    margin-top: 0;
  }
</style>
</head>
<body>
  <main class="page">
    <header class="brand">
      <span class="brand-mark"></span>
      <span class="brand-name">The Marlow Crest Advisory Services</span>
    </header>
    <div class="brand-divider"></div>

    <h1 class="connect-title">CONNECT WITH US</h1>
    <p class="connect-intro">
      Have a question or need assistance? Our liaison team is here to help.<br>
      Share your details below and we’ll get in touch with you shortly.
    </p>

    <form class="connect-form">
      <input class="field" type="text" placeholder="First Name">
      <input class="field" type="text" placeholder="Last Name">
      <input class="field" type="email" placeholder="Email Address">
      <input class="field" type="tel" placeholder="Phone Number">
      <textarea class="field field-details" placeholder="Details of your project*"></textarea>
      <button class="submit-button" type="button">Submit</button>
    </form>
  </main>
</body>
</html>
```